House-share and Room Rental Website (With Focus on the Bedroom Landing Page)

Looking for website design for our House-share (executive accommodation) and room rental business.

Our company name is: Quellnest could also be written as QuellNest or quellnest. Either is fine .. just looking for a nice clean catchy logo to go with the design.

EXAMPLES
These are examples of other websites in this field that are doing well. this is a kind of baseline.
https://dovelinter.example.au/
https://www.kestrib.example/
https://www.velunor.example/
https://www.trisbel.example/
https://www.pondmarrowseek.example.au/

Our business model is to rent rooms to people looking for high-quality accommodation. We fill the gap between those looking to rent rooms and those with rooms to rent. However, our model is slightly different from those already on the market as we looking to fill a massive gap in the market delivering upmarket rooms for rent.(Executive Accommodation) also in the back end will be coupled with a self management process in the back end.

We offer executive style accommodation that stands out above the rest. With special extras like fire safety.. and management processes that create happier homes. We are looking for a web design package that can help us grow and scale our business. We need a design that is captivating

Our MAIN focus is having a room landing page that stands out from the rest... The core of our business will rely on the promotion of the rooms in a share house... so the whole design relies on the BEDROOM landing page to drive results.

Target Market(s)

We have 2 markets we are aiming at ... the first market is people offering rooms to rent who want the highest rental return. The second market is people looking to rent safe, high-quality rooms, in houses that are well managed and looked after.

Industry/Entity Type

Share Economy

Logo Text

QuellNest

Number of Pages Required

5+ page

Font styles to use
Sans Serif

Colors
3276b5

Requirements
Must have
• A messaging system whereby we can create direct communication between those offering rooms and those looking for rooms.
• A call to action that says " Schedule an Inspection"
• Landing page for promoting rooms
• A home page for showing stock.
• Profile page for those selling rooms
• Profile page for those looking for rooms.
• A scheduling calendar for booking inspections
Nice to have
• Pages where new residents can lock in a room.. pay bond and rents.. and sign contracts
• Notifications
• SMS capabilities in the backend.
Should not have
• No script or handwriting fonts.

```html
<!DOCTYPE html>
<html lang="en">
<head>
<meta charset="utf-8">
<title>QuellNest — House-share &amp; Room Rental</title>
<link rel="stylesheet" href="https://fonts.googleapis.com/css2?family=Montserrat:wght@500;600;700&family=Poppins:wght@300;400;500;600&display=swap">
<style>
:root{
  --blue:#3276b5;
  --blue-dark:#2a63a0;
  --blue-deep:#1f5691;
  --ink:#2b2b2b;
  --text:#555;
  --muted:#8a8a8a;
  --line:#e3e6ea;
  --hero-bg:#f1f2f4;
  --night:#222426;
  --night-deep:#1a1b1c;
  --white:#fff;
}
*{box-sizing:border-box;margin:0;padding:0}
html,body{width:1200px;height:3495px;overflow:hidden}
body{font-family:"Poppins",Arial,sans-serif;color:var(--text);background:var(--white);position:relative}
h1,h2,h3,h4,.brand{font-family:"Montserrat",Arial,sans-serif;color:var(--ink)}
.abs{position:absolute}
.accent{color:var(--blue)}
svg{display:block}

/* top bar */
.topbar{position:absolute;left:508px;top:0;width:692px;height:52px;background:var(--blue);display:flex;align-items:center;color:#fff;font-size:14px}
.topbar .item{display:flex;align-items:center;gap:12px;padding-left:25px}
.topbar .item.phone{padding-left:60px}
.topbar .social{margin-left:auto;display:flex;height:100%}
.topbar .social span{width:51px;height:100%;border-left:1px solid rgba(255,255,255,.25);display:flex;align-items:center;justify-content:center}
.topbar .social span::after{content:"";width:8px;height:8px;border-radius:50%;background:#fff}

/* nav */
.brand{position:absolute;left:80px;top:52px;font-size:40px;font-weight:700;color:var(--blue-deep);letter-spacing:.5px}
.nav{position:absolute;left:303px;top:88px;display:flex;gap:22px;font-size:14px;color:#6a6a6a}
.nav a{color:inherit;text-decoration:none}
.nav a.active{color:var(--blue);font-weight:500}
.callus{position:absolute;left:855px;top:74px;display:flex;gap:10px;align-items:center;font-size:13px;color:#555;line-height:1.3}
.callus b{font-weight:500;color:#333}
.btn{display:inline-flex;align-items:center;justify-content:center;border-radius:30px;font-size:15px;font-weight:500;font-family:"Poppins",Arial,sans-serif}
.btn.solid{background:var(--blue);color:#fff}
.btn.outline{border:2px solid var(--blue);color:var(--blue);background:#fff}
.book-top{position:absolute;left:1007px;top:77px;width:114px;height:44px}

/* hero */
.hero{position:absolute;left:0;top:145px;width:1200px;height:573px;background:var(--hero-bg)}
.hero-photo{position:absolute;left:520px;top:0;width:680px;height:573px;background:linear-gradient(170deg,#6b8fb7 0%,#9fb4c9 38%,#4a4c50 58%,#b48b55 72%,#7d7f83 100%)}
.hero h1{position:absolute;left:77px;top:88px;font-size:60px;font-weight:600}
.hero p.lead{position:absolute;left:77px;top:175px;width:420px;font-size:15px;line-height:1.8;color:#555}
.hero .addr{position:absolute;left:77px;top:280px;display:flex;gap:10px;align-items:center;font-size:14px;color:#555}
.hero .inspect{position:absolute;left:77px;top:337px;width:240px;height:50px}
.stats{position:absolute;left:0;top:472px;width:520px;height:101px;background:var(--blue);display:flex;color:#fff}
.stats .stat{flex:1;display:flex;flex-direction:column;align-items:center;justify-content:center;font-size:13px;line-height:1.4}
.stats .stat svg{margin-bottom:8px}
.rent{position:absolute;left:520px;top:472px;width:188px;height:101px;background:var(--night);padding:26px 0 0 27px}
.rent small{display:block;color:#4f90d0;font-size:15px}
.rent strong{display:block;color:#fff;font-size:21px;font-weight:600;margin-top:2px}

/* welcome */
.welcome-photo{position:absolute;left:80px;top:780px;width:468px;height:408px;border-radius:200px 200px 0 0;background:radial-gradient(ellipse at 50% 55%,#e9eef4 0%,#c9d8e8 45%,#f7f8fa 80%)}
.welcome h2{position:absolute;left:606px;top:778px;font-size:34px;font-weight:600}
.welcome p{position:absolute;left:606px;top:842px;width:515px;font-size:13.5px;line-height:1.87;color:#8a8a8a}
.welcome .more{position:absolute;left:606px;top:1074px;width:133px;height:51px}

/* why */
.why{position:absolute;left:0;top:1188px;width:1200px;height:438px;background:linear-gradient(180deg,#eef3f9 0%,#b9cde2 35%,#5d8fc2 75%,#3a78b6 100%);text-align:center}
.why h2{position:absolute;left:0;right:0;top:60px;font-size:34px;font-weight:600}
.why .cols{position:absolute;left:0;top:142px;width:1200px;display:flex;justify-content:center;gap:0}
.why .col{width:362px;display:flex;flex-direction:column;align-items:center;color:#fff}
.why .icon{width:98px;height:98px;border-radius:50%;background:#fff;border:6px solid rgba(255,255,255,.5);box-shadow:0 0 0 4px rgba(50,118,181,.25);display:flex;align-items:center;justify-content:center}
.why h3{color:#fff;font-size:20px;font-weight:500;margin-top:26px}
.why p{font-size:13.5px;line-height:1.9;margin-top:8px;width:300px;color:#eef4fb}

/* gallery */
.gallery{position:absolute;left:0;top:1626px;width:1200px;height:627px;background:#fafafa}
.gallery h2{position:absolute;left:0;right:0;top:60px;text-align:center;font-size:34px;font-weight:600}
.gallery .sub{position:absolute;left:300px;width:600px;top:134px;text-align:center;font-size:13.5px;line-height:1.9;color:#9a9a9a}
.card{position:absolute;top:222px;width:333px;height:335px;background:#fff;box-shadow:0 2px 8px rgba(0,0,0,.08)}
.card .ph{height:217px}
.card h4{font-size:17px;font-weight:600;margin:28px 0 0 22px}
.card .loc{display:flex;gap:8px;align-items:center;margin:12px 0 0 22px;font-size:13px;color:#777}
.card .tag{position:absolute;left:91px;top:0;width:152px;height:40px;background:var(--blue);color:#fff;font-size:14px;font-weight:500;display:flex;align-items:center;justify-content:center}
.arrow{position:absolute;width:46px;height:46px;background:var(--blue);display:flex;align-items:center;justify-content:center}

/* amenities */
.amen{position:absolute;left:0;top:2253px;width:1200px;height:760px;background:linear-gradient(180deg,#3276b5 0%,#6a9dcc 55%,#d9e6f2 100%)}
.amen h2{position:absolute;left:77px;top:60px;font-size:34px;font-weight:600;color:#fff}
.amen .nav-arrows{position:absolute;left:1017px;top:55px;display:flex;gap:6px}
.amen .nav-arrows span{width:50px;height:50px;background:var(--blue-dark);display:flex;align-items:center;justify-content:center}
.amen .nav-arrows span.light{background:#5a93cb}
.amen-photo{position:absolute;left:77px;top:156px;width:524px;height:531px;background:linear-gradient(180deg,#8cb4e4 0%,#b7cde6 30%,#8b5a45 55%,#e8e6e0 75%,#7a8f3a 100%)}
.panel{position:absolute;left:601px;top:156px;width:522px;height:531px;background:#fff}
.panel .tag{position:absolute;left:180px;top:0;width:160px;height:46px;background:var(--blue);color:#fff;font-size:15px;font-weight:500;display:flex;align-items:center;justify-content:center}
.panel .intro{position:absolute;left:0;right:0;top:72px;text-align:center;font-size:14px;line-height:1.9;color:#777}
.panel ul{position:absolute;left:0;top:134px;width:522px;list-style:none}
.panel li{height:68px;border-bottom:1px solid var(--line);display:flex;align-items:center;font-size:15px;color:#444}
.panel li .cell{display:flex;align-items:center;gap:14px;padding-left:24px;width:265px}
.panel li .cell + .cell{padding-left:0}
.panel li:last-child{border-bottom:none}
.panel .book{position:absolute;left:0;bottom:0;width:522px;height:51px;background:var(--night);color:#fff;display:flex;align-items:center;justify-content:center;font-size:16px}

/* newsletter */
.news{position:absolute;left:0;top:3013px;width:1200px;height:105px;background:var(--blue-deep)}
.news h3{position:absolute;left:140px;top:35px;font-size:27px;font-weight:600;color:#fff}
.news .mail{position:absolute;left:77px;top:37px}
.news .field{position:absolute;left:473px;top:28px;width:438px;height:50px;border:1px solid rgba(255,255,255,.45);border-radius:4px;color:#dbe7f3;font-size:14px;padding:14px 0 0 16px}
.news .sub-btn{position:absolute;left:925px;top:28px;width:197px;height:50px;background:#fff;border-radius:4px;color:var(--ink);font-size:16px;font-weight:500;display:flex;align-items:center;justify-content:center}

/* footer */
.footer{position:absolute;left:0;top:3118px;width:1200px;height:312px;background:var(--night);color:#ddd}
.footer .brand{position:absolute;left:106px;top:82px;font-size:36px;color:#fff}
.footer .about{position:absolute;left:77px;top:168px;width:250px;font-size:13px;line-height:1.9;color:#ddd}
.footer h4{position:absolute;top:62px;font-size:19px;font-weight:600;color:#4f90d0}
.footer .article{position:absolute;left:348px;font-size:14px;color:#fff;font-weight:500}
.footer .article small{display:block;font-size:12px;color:#999;font-weight:400;margin-top:4px}
.footer .contact{position:absolute;left:616px;display:flex;gap:14px;font-size:13.5px;color:#ddd;line-height:1.8}
.footer .thumbs{position:absolute;left:884px;top:110px;display:grid;grid-template-columns:repeat(3,60px);gap:15px 12px}
.footer .thumbs span{height:60px;border:3px solid #eee}
.copy{position:absolute;left:0;top:3430px;width:1200px;height:65px;background:var(--night-deep);color:#bbb;font-size:13px;display:flex;align-items:center;justify-content:center}
</style>
</head>
<body>

<header>
  <div class="topbar">
    <div class="item">
      <svg width="20" height="14" viewBox="0 0 20 14"><rect x="1" y="1" width="18" height="12" fill="none" stroke="#fff" stroke-width="1.6"/><path d="M1 1l9 7 9-7" fill="none" stroke="#fff" stroke-width="1.6"/></svg>
      <span>info@quellnest.com</span>
    </div>
    <div class="item phone">
      <svg width="16" height="16" viewBox="0 0 24 24"><path d="M6.6 10.8a15 15 0 006.6 6.6l2.2-2.2a1 1 0 011-.25 11.4 11.4 0 003.6.6 1 1 0 011 1V20a1 1 0 01-1 1A17 17 0 013 4a1 1 0 011-1h3.5a1 1 0 011 1c0 1.25.2 2.45.6 3.6a1 1 0 01-.25 1z" fill="#fff"/></svg>
      <span>123.456.7890</span>
    </div>
    <div class="social" aria-label="Social links"><span></span><span></span><span></span><span></span></div>
  </div>

  <div class="brand">QuellNest</div>

  <nav class="nav">
    <a class="active">Home</a><a>About The Bedroom</a><a>Gallery</a><a>Latest Offers</a><a>Blog</a><a>Availability</a>
  </nav>

  <div class="callus">
    <svg width="30" height="34" viewBox="0 0 24 24"><path d="M6.6 10.8a15 15 0 006.6 6.6l2.2-2.2a1 1 0 011-.25 11.4 11.4 0 003.6.6 1 1 0 011 1V20a1 1 0 01-1 1A17 17 0 013 4a1 1 0 011-1h3.5a1 1 0 011 1c0 1.25.2 2.45.6 3.6a1 1 0 01-.25 1z" fill="#3276b5"/></svg>
    <div>Call Us<br><b>123.456.7890</b></div>
  </div>
  <a class="btn solid book-top">Book Now</a>
</header>

<section class="hero">
  <h1><span class="accent">Quell</span>Nest</h1>
  <p class="lead">Lorem ipsum dolor sit amet, consectetur adipiscing elit, sed do eiusmod tempor incididunt ut labore et dolore magna aliqua.</p>
  <div class="addr">
    <svg width="16" height="20" viewBox="0 0 16 20"><path d="M8 0a7 7 0 00-7 7c0 5 7 13 7 13s7-8 7-13a7 7 0 00-7-7zm0 9.5A2.5 2.5 0 118 4.5a2.5 2.5 0 010 5z" fill="#3276b5"/></svg>
    <span>123, Address,Street, State,City &nbsp;|&nbsp; 455001</span>
  </div>
  <a class="btn outline inspect">Schedule an Inspection</a>

  <div class="hero-photo" role="img" aria-label="Photo of a modern two-storey house with lit windows and a double garage at dusk"></div>

  <div class="stats">
    <div class="stat">
      <svg width="26" height="20" viewBox="0 0 26 20"><path d="M2 2v16M2 12h22v6M24 12V9a3 3 0 00-3-3H11v6" fill="none" stroke="#fff" stroke-width="2"/><circle cx="6.5" cy="8.5" r="2.5" fill="#fff"/></svg>
      <span>2</span><span>Allowed</span>
    </div>
    <div class="stat">
      <svg width="22" height="20" viewBox="0 0 22 20"><path d="M2 10h18v5H2zM4 15v3M18 15v3M3 10V4a2 2 0 012-2h12a2 2 0 012 2v6" fill="none" stroke="#fff" stroke-width="2"/></svg>
      <span>3</span><span>Allowed</span>
    </div>
    <div class="stat">
      <svg width="22" height="20" viewBox="0 0 22 20"><path d="M11 2l9 7v9H2V9z" fill="none" stroke="#fff" stroke-width="2"/><rect x="8" y="11" width="6" height="7" fill="none" stroke="#fff" stroke-width="2"/></svg>
      <span>3500</span><span>Allowed</span>
    </div>
    <div class="stat">
      <svg width="22" height="20" viewBox="0 0 22 20"><circle cx="11" cy="13" r="5" fill="#fff"/><circle cx="4" cy="7" r="2.2" fill="#fff"/><circle cx="8.5" cy="3" r="2.2" fill="#fff"/><circle cx="13.5" cy="3" r="2.2" fill="#fff"/><circle cx="18" cy="7" r="2.2" fill="#fff"/></svg>
      <span>Pets</span><span>Allowed</span>
    </div>
    <div class="stat">
      <svg width="18" height="22" viewBox="0 0 18 22"><path d="M6 2h6l-2 4h-2zM9 6c-5 3-7 7-7 10a7 5 0 0014 0c0-3-2-7-7-10z" fill="#fff"/></svg>
      <span>$2,500</span><span>Allowed</span>
    </div>
  </div>
  <div class="rent"><small>Rent Price</small><strong>$ 2,199 / mo.</strong></div>
</section>

<section class="welcome">
  <div class="welcome-photo" role="img" aria-label="Photo of a smiling family of four in light blue clothing"></div>
  <h2>Welcome to <span class="accent">QuellNest</span></h2>
  <p>Lorem ipsum dolor sit amet, consectetur adipiscing elit, sed do eiusmod tempor incididunt ut labore et dolore magna aliqua. Ut enim ad minim the veniam, quis nostrud exercitation ullamco laboris nisi ut aliquip ex ea they commodo consequat. Duis aute irure dolor in reprehenderit in voluptate velit esse cillum dolore eu fugiat nulla pariatur. Excepteur sint occaecat cupidatat non proident, sunt in culpa qui officia deserunt mollit anim id est laborum. Sed ut perspiciatis unde omnis iste natus error sit voluptatem accusantium doloremque laudantium.</p>
  <a class="btn solid more">Read More</a>
</section>

<section class="why" role="region" aria-label="Why choose us, over a softly blurred bedroom photo in blue tones">
  <h2>Why <span class="accent">Choose Us</span></h2>
  <div class="cols">
    <div class="col">
      <div class="icon"><svg width="42" height="42" viewBox="0 0 42 42"><path d="M4 38h34M8 38V16l13-10 13 10v22" fill="none" stroke="#3276b5" stroke-width="2.5"/><path d="M14 20h5v5h-5zM23 20h5v5h-5zM14 29h5v5h-5zM23 29h5v9h-5z" fill="#3276b5"/></svg></div>
      <h3>Find your room</h3>
      <p>Lorem ipsum dolor sit amet, consectetur adipiscing elit, sed do eiusmod incididunt ut labore et dolore magna aliqua.</p>
    </div>
    <div class="col">
      <div class="icon"><svg width="42" height="42" viewBox="0 0 42 42"><circle cx="21" cy="14" r="8" fill="none" stroke="#3276b5" stroke-width="2.5"/><path d="M6 38c0-9 7-14 15-14s15 5 15 14z" fill="none" stroke="#3276b5" stroke-width="2.5"/></svg></div>
      <h3>Meet the flatmates</h3>
      <p>Lorem ipsum dolor sit amet, consectetur adipiscing elit, sed do eiusmod incididunt ut labore et dolore magna aliqua.</p>
    </div>
    <div class="col">
      <div class="icon"><svg width="42" height="42" viewBox="0 0 42 42"><path d="M21 6c9 0 16 6 16 13s-7 13-16 13c-2 0-4-.3-6-1l-8 4 2-7c-2-2.4-4-5.6-4-9C5 12 12 6 21 6z" fill="none" stroke="#3276b5" stroke-width="2.5"/><circle cx="14" cy="19" r="2" fill="#3276b5"/><circle cx="21" cy="19" r="2" fill="#3276b5"/><circle cx="28" cy="19" r="2" fill="#3276b5"/></svg></div>
      <h3>We're here to help</h3>
      <p>Lorem ipsum dolor sit amet, consectetur adipiscing elit, sed do eiusmod incididunt ut labore et dolore magna aliqua.</p>
    </div>
  </div>
</section>

<section class="gallery">
  <h2>Our <span class="accent">Gallery</span></h2>
  <p class="sub">Lorem ipsum dolor sit amet, consectetur adipiscing elit, sed do eiusmod tempor exercitation ullamco laboris nisi ut aliquip ex ea they commodo consequat.</p>

  <div class="arrow" style="left:30px;top:419px"><svg width="12" height="16" viewBox="0 0 12 16"><path d="M9 2L3 8l6 6" fill="none" stroke="#fff" stroke-width="2.5"/></svg></div>

  <article class="card" style="left:77px">
    <div class="ph" role="img" aria-label="Photo of a warm-lit bedroom with a large bed and curtains" style="background:linear-gradient(180deg,#3a3430,#8a6c50 50%,#c9b79c)"></div>
    <h4>Modern Home in A Residential</h4>
    <div class="loc"><svg width="12" height="16" viewBox="0 0 16 20"><path d="M8 0a7 7 0 00-7 7c0 5 7 13 7 13s7-8 7-13a7 7 0 00-7-7zm0 9.5A2.5 2.5 0 118 4.5a2.5 2.5 0 010 5z" fill="#3276b5"/></svg>123, Address,Street, State,City.</div>
  </article>
  <article class="card" style="left:433px">
    <div class="ph" role="img" aria-label="Photo of a white modern house with a pool and lawn" style="background:linear-gradient(180deg,#a9c6e6,#e8eef3 40%,#8aa1b6 65%,#6f9a3e)"></div>
    <div class="tag">$3000 PER WEEK</div>
    <h4 class="accent">Modern Home in A Residential</h4>
    <div class="loc"><svg width="12" height="16" viewBox="0 0 16 20"><path d="M8 0a7 7 0 00-7 7c0 5 7 13 7 13s7-8 7-13a7 7 0 00-7-7zm0 9.5A2.5 2.5 0 118 4.5a2.5 2.5 0 010 5z" fill="#3276b5"/></svg>123, Address,Street, State,City.</div>
  </article>
  <article class="card" style="left:790px">
    <div class="ph" role="img" aria-label="Photo of a bright bedroom with navy walls and a window onto trees" style="background:linear-gradient(135deg,#6f8fa8,#c7d5de 45%,#3e4f6a 70%,#eef1f4)"></div>
    <h4>Modern Home in A Residential</h4>
    <div class="loc"><svg width="12" height="16" viewBox="0 0 16 20"><path d="M8 0a7 7 0 00-7 7c0 5 7 13 7 13s7-8 7-13a7 7 0 00-7-7zm0 9.5A2.5 2.5 0 118 4.5a2.5 2.5 0 010 5z" fill="#3276b5"/></svg>123, Address,Street, State,City.</div>
  </article>

  <div class="arrow" style="left:1124px;top:419px"><svg width="12" height="16" viewBox="0 0 12 16"><path d="M3 2l6 6-6 6" fill="none" stroke="#fff" stroke-width="2.5"/></svg></div>
</section>

<section class="amen">
  <h2>Room Amenities</h2>
  <div class="nav-arrows">
    <span><svg width="12" height="16" viewBox="0 0 12 16"><path d="M9 2L3 8l6 6" fill="none" stroke="#fff" stroke-width="2.5"/></svg></span>
    <span class="light"><svg width="12" height="16" viewBox="0 0 12 16"><path d="M3 2l6 6-6 6" fill="none" stroke="#fff" stroke-width="2.5"/></svg></span>
  </div>
  <div class="amen-photo" role="img" aria-label="Photo of a red-brick house with a grey tiled roof and white garage doors"></div>
  <div class="panel">
    <div class="tag">$3000 PER WEEK</div>
    <p class="intro">These are some things that may be<br>included in the room</p>
    <ul>
      <li><div class="cell"><svg width="28" height="24" viewBox="0 0 28 24"><path d="M2 22V10h24v12M2 16h24M6 10V4h16v6" fill="none" stroke="#3276b5" stroke-width="1.8"/></svg>Furnished/unfurnished</div></li>
      <li><div class="cell"><svg width="28" height="24" viewBox="0 0 28 24"><path d="M2 8h24M5 8v14M23 8v14M14 8V2h8" fill="none" stroke="#3276b5" stroke-width="1.8"/></svg>Study Desk / Workstation</div></li>
      <li><div class="cell"><svg width="28" height="24" viewBox="0 0 28 24"><path d="M14 2l11 8v12H3V10z" fill="none" stroke="#3276b5" stroke-width="1.8"/><rect x="9" y="13" width="10" height="9" fill="none" stroke="#3276b5" stroke-width="1.8"/></svg>Storage space</div></li>
      <li><div class="cell"><svg width="28" height="24" viewBox="0 0 28 24"><path d="M2 12h24v4a5 5 0 01-5 5H7a5 5 0 01-5-5zM5 12V4a2 2 0 014 0" fill="none" stroke="#3276b5" stroke-width="1.8"/></svg>Ensuite shower</div><div class="cell"><svg width="28" height="24" viewBox="0 0 28 24"><rect x="2" y="4" width="24" height="15" fill="none" stroke="#3276b5" stroke-width="1.8"/><path d="M10 22h8" stroke="#3276b5" stroke-width="1.8"/></svg>TV</div></li>
      <li><div class="cell"><svg width="28" height="24" viewBox="0 0 28 24"><rect x="6" y="2" width="16" height="20" fill="none" stroke="#3276b5" stroke-width="1.8"/><path d="M14 2v20M11 11v3M17 11v3" stroke="#3276b5" stroke-width="1.8"/></svg>Wardrobe</div><div class="cell"><svg width="28" height="24" viewBox="0 0 28 24"><path d="M2 10h24v12H2zM2 16h24M9 10v12M19 10v12M6 10V4h16v6" fill="none" stroke="#3276b5" stroke-width="1.8"/></svg>Kitchenette</div></li>
    </ul>
    <div class="book">Book Now</div>
  </div>
</section>

<section class="news">
  <svg class="mail" width="44" height="32" viewBox="0 0 44 32"><rect x="2" y="2" width="40" height="28" fill="none" stroke="#fff" stroke-width="2.5"/><path d="M2 2l20 16L42 2M2 30l14-14M42 30L28 16" fill="none" stroke="#fff" stroke-width="2.5"/></svg>
  <h3>Sign In To Newsletter</h3>
  <div class="field">Email Address....</div>
  <div class="sub-btn">Subscribe Now</div>
</section>

<footer class="footer">
  <div class="brand">QuellNest</div>
  <p class="about">Lorem ipsum dolor sit amet, typeing ullamco laboris nisi ut aliquip ex ea they commodo consequat.</p>

  <h4 style="left:348px">Latest Article</h4>
  <div class="article" style="top:112px">Lorem ipsum dolor sit amet,<small>20 February 2019</small></div>
  <div class="article" style="top:170px">Lorem ipsum dolor sit amet,<small>20 February 2019</small></div>
  <div class="article" style="top:228px">Lorem ipsum dolor sit amet,<small>20 February 2019</small></div>

  <h4 style="left:616px">Get In Touch</h4>
  <div class="contact" style="top:114px"><svg width="16" height="16" viewBox="0 0 24 24"><path d="M6.6 10.8a15 15 0 006.6 6.6l2.2-2.2a1 1 0 011-.25 11.4 11.4 0 003.6.6 1 1 0 011 1V20a1 1 0 01-1 1A17 17 0 013 4a1 1 0 011-1h3.5a1 1 0 011 1c0 1.25.2 2.45.6 3.6a1 1 0 01-.25 1z" fill="#4f90d0"/></svg>123.56.7890</div>
  <div class="contact" style="top:164px"><svg width="16" height="14" viewBox="0 0 20 14"><rect width="20" height="14" fill="#4f90d0"/><path d="M0 0l10 7 10-7" fill="none" stroke="#222426" stroke-width="1.6"/></svg>info@quellnest.com</div>
  <div class="contact" style="top:212px"><svg width="14" height="18" viewBox="0 0 16 20"><path d="M8 0a7 7 0 00-7 7c0 5 7 13 7 13s7-8 7-13a7 7 0 00-7-7zm0 9.5A2.5 2.5 0 118 4.5a2.5 2.5 0 010 5z" fill="#4f90d0"/></svg><span>123, Address, State Name,<br>City Name,Zipcode</span></div>

  <h4 style="left:884px">Image Galley</h4>
  <div class="thumbs">
    <span role="img" aria-label="House thumbnail" style="background:linear-gradient(#9bb8d6,#b69a72)"></span>
    <span role="img" aria-label="House thumbnail" style="background:linear-gradient(#a8c2de,#7b8a5a)"></span>
    <span role="img" aria-label="House thumbnail" style="background:linear-gradient(#5b5f66,#b28a54)"></span>
    <span role="img" aria-label="House thumbnail" style="background:linear-gradient(#b4c9df,#8c6f58)"></span>
    <span role="img" aria-label="House thumbnail" style="background:linear-gradient(#c4d3e2,#90a06a)"></span>
    <span role="img" aria-label="House thumbnail" style="background:linear-gradient(#9fb6cf,#e5e2dc)"></span>
  </div>
</footer>
<div class="copy">Copyright © QuellNest - 2019 . All Right Reserved</div>

</body>
</html>
```